"Turn The Light" Dance Production Poster

This is a dance school annual theatre performance, at the Holloway Grand Theatre. The dates are from the 26th-28th July 2012, and the show is called "Turn The Light."

Although not themed around Desmond Harlow specifically, we are using a few songs hence the title.

We need an eye catching poster with out focusing too much around DH. Maybe even using his theme/image subliminally but must look professional and vivid.

We are a dance school predominantly female based with a few males - age range 2-55
Updates

Hi guys - please check brief 

We are getting to many designs based too much around Desmond Harlow

This only has to be subliminal as the show isn't about him, it's mainly a generic dance show

Please try to bare this in mind

Thanks

Target Market(s)

Parents, family, friends of the performers/general public

Industry/Entity Type

School

Requirements
Must have
• The Wendell Moss School Of Dance Present "Turn The Light"
26th-28th July 2012 at the Holloway Grand

Tickets available from the Theatre Box Office

www.wmschoolofdance-example.co.uk

Nice to have
• Subliminal Desmond Harlow feel - no pictures of him though
Should not have
• Cheap templates, poor images, flowery fonts

```html
<!DOCTYPE html>
<html lang="en">
<head>
<meta charset="utf-8">
<title>Turn The Light – The Wendell Moss School Of Dance</title>
<link rel="stylesheet" href="https://fonts.googleapis.com/css2?family=Bungee&family=Roboto:wght@300;400;700&display=swap">
<style>
  :root {
    --night: #05070d;
    --deep-blue: #0b2340;
    --stage-blue: #17507a;
    --teal-glow: #2aa3b8;
    --haze: #9fc4d6;
    --ink-white: #ffffff;
    --title-white: rgba(246, 248, 250, 0.93);
  }
  html, body {
    margin: 0;
    padding: 0;
    width: 1200px;
    height: 848px;
    overflow: hidden;
    background: var(--night);
  }
  .poster {
    position: relative;
    width: 1200px;
    height: 848px;
    overflow: hidden;
    font-family: "Roboto", Arial, sans-serif;
    color: var(--ink-white);
  }
  .stage-lights {
    position: absolute;
    inset: 0;
    background:
      radial-gradient(ellipse 260px 420px at 170px 560px, rgba(159,196,214,0.35), transparent 70%),
      radial-gradient(ellipse 260px 420px at 1060px 560px, rgba(159,196,214,0.35), transparent 70%),
      radial-gradient(ellipse 520px 300px at 600px 720px, rgba(42,163,184,0.35), transparent 70%),
      radial-gradient(ellipse 700px 380px at 600px 420px, rgba(42,163,184,0.35), transparent 75%),
      linear-gradient(180deg, var(--night) 0%, #081526 20%, var(--deep-blue) 45%, var(--stage-blue) 75%, #0d3356 100%);
  }
  .presenter {
    position: absolute;
    top: 22px;
    left: 0;
    width: 1200px;
    margin: 0;
    text-align: center;
    font-weight: 400;
    font-size: 28px;
    letter-spacing: 0.2em;
    text-transform: uppercase;
  }
  .show-title {
    position: absolute;
    top: 222px;
    left: 0;
    width: 1200px;
    margin: 0;
    text-align: center;
    font-family: "Bungee", "Arial Black", sans-serif;
    font-weight: 400;
    font-size: 150px;
    line-height: 190px;
    letter-spacing: -0.02em;
    color: var(--title-white);
    text-transform: uppercase;
  }
  .show-title span { display: block; }
  .details {
    position: absolute;
    top: 712px;
    left: 0;
    width: 1200px;
    text-align: center;
    font-size: 28px;
    font-weight: 300;
    line-height: 38px;
  }
  .details p { margin: 0; }
  .details .website { font-weight: 700; letter-spacing: 0.02em; }
</style>
</head>
<body>
  <main class="poster">
    <div class="stage-lights" role="img" aria-label="Photograph of blue stage spotlights shining down through haze"></div>
    <p class="presenter">The Wendell Moss School Of Dance Present</p>
    <h1 class="show-title"><span>Turn The</span><span>Light</span></h1>
    <div class="details">
      <p>26th-28th July 2012 at the Holloway Grand</p>
      <p>Tickets available from the Theatre Box Office</p>
      <p class="website">www.wmschoolofdance-example.co.uk</p>
    </div>
  </main>
</body>
</html>
```